Product Label & Logo for New Supplement

Your design will automatically be eliminated if you do NOT read this brief, because the description tells you about the brand you will be creating an identity for.Attached is the current label for the product. It is boring and doesn’t tell a story.We need you to unleash creative work to help patients with chronic pain diseases - like Multiple Sclerosis, Chronic Fatigue Syndrome, Lupus, and Fibromyalgia - no longer be defined by their disease. Qorvi Blend is a new supplement developed by a neurologist to help patients with chronic pain feel better and have better days. It increases energy and stamina, saving the patient from having to take upwards of 40 different supplements.The label and logo need to convey that this supplement will give hurting patients new life.
Updates
Went on vacation/holiday
Target Market(s)
People with fatigue, pain and inflammation
Industry/Entity Type
Supplement
Requirements
Must have
- Gender neutral, eye catching, all the ingredients listed in addition to logo design
Nice to have
- Custom logo, no generic fonts for name brand

```html
<!DOCTYPE html>
<html lang="en">
<head>
<meta charset="utf-8">
<title>Qorvi Blend – Supplement Label</title>
<link href="https://fonts.googleapis.com/css2?family=Oswald:wght@500;600&family=Arimo:wght@400;700&display=swap" rel="stylesheet">
<style>
  :root {
    --page: #ffffff;
    --label-bg: #05071a;
    --ink-light: #ffffff;
    --ink-dark: #05071a;
    --cyan: #00ffff;
    --glow-blue: #1e6bff;
    --glow-core: #bfe9ff;
    --warm: #e0642a;
  }
  * { box-sizing: border-box; margin: 0; padding: 0; }
  html, body {
    width: 1200px; height: 1183px; overflow: hidden;
    background: var(--page);
  }
  .label {
    position: absolute; left: 40px; top: 358px;
    width: 1120px; height: 466px;
    background: var(--label-bg);
    color: var(--ink-light);
    font-family: "Arimo", Arial, sans-serif;
    overflow: hidden;
  }
  .story {
    position: absolute; left: 43px; top: 36px; width: 250px;
    font-size: 12.4px; line-height: 15.6px; text-align: justify;
  }
  .story p + p { margin-top: 15.6px; }
  .info-box {
    position: absolute; left: 45px; top: 311px; width: 168px; height: 95px;
    background: var(--ink-light);
  }
  .recycle { position: absolute; left: 230px; top: 377px; width: 28px; height: 28px; }
  .hero-art {
    position: absolute; left: 295px; top: 0; width: 527px; height: 346px;
    background: radial-gradient(circle at 50% 47%, rgba(30,107,255,.55) 0%, rgba(30,107,255,.25) 38%, rgba(5,7,26,0) 70%);
  }
  .hero-art svg { width: 100%; height: 100%; display: block; }
  .brand-name {
    position: absolute; left: 300px; width: 520px; top: 328px;
    text-align: center;
    font-family: "Oswald", Arial, sans-serif; font-weight: 600;
    font-size: 52px; line-height: 60px; letter-spacing: 1px;
    text-transform: uppercase; color: var(--ink-light);
  }
  .count {
    position: absolute; left: 455px; width: 200px; top: 398px;
    text-align: center;
    font-family: "Oswald", Arial, sans-serif; font-weight: 500;
    font-size: 21px; line-height: 28px; letter-spacing: .5px;
  }
  .band {
    position: absolute; left: 0; right: 0; top: 430px; height: 36px;
    background: var(--cyan); color: var(--ink-dark);
    display: flex; align-items: center; justify-content: center;
    font-family: "Oswald", Arial, sans-serif; font-weight: 600;
    font-size: 19px; letter-spacing: 3px;
  }
  .facts { position: absolute; left: 821px; top: 36px; width: 266px; }
  .facts-title {
    font-family: "Oswald", Arial, sans-serif; font-weight: 500;
    font-size: 19px; line-height: 24px;
  }
  .serving { margin-top: 8px; font-weight: 700; font-size: 12.6px; line-height: 15.6px; }
  .nutrient-table {
    margin-top: 13px; width: 266px; border-collapse: collapse;
    border: 2px solid var(--ink-light); font-size: 12.6px;
  }
  .nutrient-table th {
    background: var(--ink-light); color: var(--ink-dark);
    font-weight: 700; height: 46px; line-height: 15px;
    border-left: 2px solid var(--label-bg);
  }
  .nutrient-table th:first-child { border-left: none; }
  .nutrient-table td {
    height: 26px; text-align: center;
    border-left: 2px solid var(--ink-light);
  }
  .nutrient-table td.name { text-align: left; padding-left: 5px; border-left: none; }
  .nutrient-table tr:first-child td { padding-top: 4px; }
  .nutrient-table tr:last-child td { padding-bottom: 10px; height: 34px; }
  .col-name { width: 125px; }
  .col-amount { width: 80px; }
  .facts-note {
    margin-top: 11px; width: 268px;
    font-weight: 700; font-size: 12.6px; line-height: 15.6px; text-align: justify;
  }
</style>
</head>
<body>
  <main class="label">
    <section class="story">
      <p>Lorem ipsum dolor sit amet, consectetuer adipiscing elit, sed diam nonummy nibh euismod tincidunt ut laoreet dolore magna aliquam erat volutpat. Ut wisi enim ad minim veniam, quis nostrud exerci tation ullamcorper suscipit lobortis nisl ut aliquip ex ea commodo consequat.</p>
      <p>Lorem ipsum dolor sit amet, cons ectetuer adipiscing elit, sed diam nonummy nibh euismod tincidunt ut laoreet dolore magna iquip ex ea commodo consequat.</p>
      <p>Lorem ipsum dolor sit amet, consectetuer adipiscing elit, sed diam nonummy nibh euismod tincidunt ut laoreet dolore magna</p>
    </section>

    <div class="info-box"></div>
    <svg class="recycle" viewBox="0 0 24 24" aria-hidden="true">
      <g fill="none" stroke="#fff" stroke-width="2.4" stroke-linecap="round" stroke-linejoin="round">
        <path d="M9 5 L12 2.5 L15 5"/><path d="M12 3 L16.5 10.5"/>
        <path d="M20 14 L21 18 L17 19"/><path d="M20.5 18 L11.5 18"/>
        <path d="M6 20 L2.5 17.5 L4 13.5"/><path d="M3 17 L7.5 9.5"/>
      </g>
    </svg>

    <div class="hero-art" role="img" aria-label="Illustration of a glowing human head with a highlighted brain, framed by a circle of blue electric lightning">
      <svg viewBox="0 0 527 346" aria-hidden="true">
        <defs>
          <radialGradient id="portrait" cx="50%" cy="50%" r="50%">
            <stop offset="0%" stop-color="#ffb347"/>
            <stop offset="45%" stop-color="#b8431c"/>
            <stop offset="100%" stop-color="#2a1a1a"/>
          </radialGradient>
        </defs>
        <circle cx="266" cy="163" r="118" fill="url(#portrait)"/>
        <circle cx="266" cy="163" r="121" fill="none" stroke="#9ff3ff" stroke-width="5"/>
      </svg>
    </div>

    <h1 class="brand-name">Qorvi Blend</h1>
    <p class="count">60 TABLETS</p>

    <aside class="facts">
      <h2 class="facts-title">LOREM IPSUM DOLOR SIT</h2>
      <p class="serving">Serving size: 1 capsule<br>Servings per container 60</p>
      <table class="nutrient-table">
        <thead>
          <tr><th class="col-name"></th><th class="col-amount">Amount per serving</th><th>% NRV</th></tr>
        </thead>
        <tbody>
          <tr><td class="name">Sodium</td><td>120mg</td><td>6%</td></tr>
          <tr><td class="name">Chloride</td><td>180mg</td><td>6%</td></tr>
          <tr><td class="name">Calcium Chelate</td><td>100mg</td><td>10%</td></tr>
          <tr><td class="name">Magnesium Chelate</td><td>50mg</td><td>12%</td></tr>
          <tr><td class="name">Potassium Chelate</td><td>75mg</td><td>1.5%</td></tr>
          <tr><td class="name">Manganese Chelate</td><td>0.5mg</td><td>25%</td></tr>
          <tr><td class="name">Ginger Root Extract</td><td>8mg</td><td>N/A</td></tr>
        </tbody>
      </table>
      <p class="facts-note">Lorem ipsum dolor sit amet, consectetuer adipiscing elit, sed diam nonummy nibh laoreet dolore magna</p>
    </aside>

    <div class="band">DIATERY SUPPLEMENT</div>
  </main>
</body>
</html>
```